Create modern and sleek business card for luxury real estate company

We're a "boutique" real estate office looking for a design that gets across a highly modern luxury brand. Blacks and whites are probably the best colors unless we try a silver foil for the logo. I've attached a version of our current logo here. I'd like to swap out the current font on there with Gotham Light Regular.

I'm looking to have one side of the card have the logo with the space for our agents info on the other side.

Target Market(s)

Young professionals in a "luxury" headspace

Industry/Entity Type

Real estate

Contact Information for Business Card

A place for agent name, cell number, website. The slogan "Simply Rethinking Real Estate".

Font styles to use
Other font styles liked:
• Gotham Regular

Colors

Designer to choose only greyscale colors for use in the design.

Requirements
Must have
• Matte black as the background color. Clean lines and use of contrast. A specific design aspect that will use silver foil.
Nice to have
• Up in the air on integrating a QR code
Should not have
• Any houses or other real estate related design (ex: a clip art house)

```html
<!DOCTYPE html>
<html lang="en">
<head>
<meta charset="utf-8">
<title>Lumen Estates – Business Card</title>
<link href="https://fonts.googleapis.com/css2?family=Montserrat:wght@300;400;600&display=swap" rel="stylesheet">
<style>
  :root {
    --backdrop: #e2e0e1;
    --card: #1c1b19;
    --band: #000000;
    --ink: #ffffff;
    --silver: #cfcfcf;
    --shadow: rgba(0, 0, 0, 0.28);
  }
  * { margin: 0; padding: 0; box-sizing: border-box; }
  html, body {
    width: 1200px;
    height: 2303px;
    overflow: hidden;
    background: var(--backdrop);
    font-family: "Montserrat", "Helvetica Neue", Arial, sans-serif;
  }
  .stage {
    position: relative;
    width: 1200px;
    height: 2303px;
  }
  .card {
    position: absolute;
    left: 100px;
    width: 1000px;
    height: 600px;
    background: var(--card);
    box-shadow: 0 18px 50px var(--shadow);
    overflow: hidden;
    color: var(--ink);
  }
  .card--front { top: 520px; }
  .card--back { top: 1183px; }

  .front-arc { position: absolute; inset: 0; }

  .agent {
    position: absolute;
    left: 56px;
    top: 256px;
  }
  .agent-name {
    font-size: 46px;
    font-weight: 300;
    letter-spacing: 1px;
    line-height: 1;
  }
  .agent-name strong { font-weight: 600; }
  .agent-role {
    margin-top: 18px;
    font-size: 23px;
    font-weight: 300;
    letter-spacing: 1px;
  }

  .contact {
    position: absolute;
    left: 574px;
    list-style: none;
  }
  .contact-item {
    display: flex;
    align-items: center;
    height: 52px;
    margin-bottom: 40px;
  }
  .contact-icon { width: 52px; height: 52px; flex: none; }
  .contact-text {
    margin-left: 36px;
    font-size: 24px;
    font-weight: 300;
    letter-spacing: 1px;
  }
  .contact { top: 248px; }

  .band {
    position: absolute;
    left: 0;
    width: 100%;
    background: var(--band);
  }
  .band--top { top: 0; height: 117px; border-bottom: 3px solid var(--ink); }
  .band--bottom { bottom: 0; height: 117px; border-top: 3px solid var(--ink); }

  .brand {
    position: absolute;
    left: 222px;
    top: 228px;
    display: flex;
    align-items: center;
  }
  .brand-mark {
    width: 144px;
    height: 144px;
    border: 3px solid var(--silver);
    border-radius: 50%;
    flex: none;
  }
  .brand-name {
    margin-left: 30px;
    font-size: 64px;
    font-weight: 300;
    line-height: 1.08;
    letter-spacing: 2px;
    color: var(--silver);
  }
</style>
</head>
<body>
<main class="stage">

  <section class="card card--front" aria-label="Card front: agent details">
    <svg class="front-arc" width="1000" height="600" viewBox="0 0 1000 600" aria-hidden="true">
      <circle cx="224" cy="300" r="312" fill="none" stroke="#ffffff" stroke-width="3"/>
    </svg>

    <div class="agent">
      <p class="agent-name"><strong>ADAM</strong> KELLER</p>
      <p class="agent-role">CREATIVE DESIGNER</p>
    </div>

    <ul class="contact">
      <li class="contact-item">
        <svg class="contact-icon" viewBox="0 0 52 52" aria-hidden="true">
          <circle cx="26" cy="26" r="24" fill="none" stroke="#fff" stroke-width="2"/>
          <rect x="19" y="14" width="14" height="24" rx="2" fill="none" stroke="#fff" stroke-width="2"/>
          <line x1="19" y1="33" x2="33" y2="33" stroke="#fff" stroke-width="1.5"/>
          <circle cx="26" cy="35.5" r="1.2" fill="#fff"/>
        </svg>
        <span class="contact-text">+0914370258</span>
      </li>
      <li class="contact-item">
        <svg class="contact-icon" viewBox="0 0 52 52" aria-hidden="true">
          <circle cx="26" cy="26" r="24" fill="none" stroke="#fff" stroke-width="2"/>
          <circle cx="26" cy="26" r="13" fill="none" stroke="#fff" stroke-width="2"/>
          <ellipse cx="26" cy="26" rx="6" ry="13" fill="none" stroke="#fff" stroke-width="1.5"/>
          <line x1="13" y1="26" x2="39" y2="26" stroke="#fff" stroke-width="1.5"/>
          <line x1="15" y1="20" x2="37" y2="20" stroke="#fff" stroke-width="1.5"/>
          <line x1="15" y1="32" x2="37" y2="32" stroke="#fff" stroke-width="1.5"/>
        </svg>
        <span class="contact-text">harborlanehomes.com</span>
      </li>
    </ul>
  </section>

  <section class="card card--back" aria-label="Card back: brand">
    <div class="band band--top"></div>
    <div class="brand">
      <div class="brand-mark" aria-hidden="true"></div>
      <p class="brand-name">LUMEN<br>ESTATES</p>
    </div>
    <div class="band band--bottom"></div>
  </section>

</main>
</body>
</html>
```